Kestrel Bridge Consulting (KBC) Business Card Design

I would like to create double-sided business cards that contain:
1) Name: Derek Molvane
2) Phone Number: +1 (555) 218-4907
3) Email: Derek.Molvane@KestrelBridgeConsulting.example
4) Website: KestrelBridgeConsulting.example

I would like to include my logo and a color scheme similar to the Varnholt Grand Prix Ostera squad color scheme (black, silver, greenish-blue – but can also include regular blue)

What we do: Our company develops and delivers innovative and pragmatic information technology and cybersecurity risk and compliance solutions for organizations in the commercial market as well as the federal, and state/local sectors.

```html
<!DOCTYPE html>
<html lang="en">
<head>
<meta charset="utf-8">
<title>Kestrel Bridge Consulting — Business Cards</title>
<link rel="stylesheet" href="https://fonts.googleapis.com/css2?family=Montserrat:wght@400;500;700&display=swap">
<style>
  :root {
    --bg: #d6d6d6;
    --card: #f4f4f4;
    --cyan: #3fb3d9;
    --blue: #1d64b8;
    --ink: #141414;
    --card-w: 640px;
    --card-h: 366px;
  }
  * { box-sizing: border-box; margin: 0; padding: 0; }
  html, body { width: 1200px; height: 1051px; overflow: hidden; }
  body {
    background: var(--bg);
    font-family: "Montserrat", Arial, sans-serif;
    color: var(--ink);
    position: relative;
  }
  .card {
    position: absolute;
    left: 280px;
    width: var(--card-w);
    height: var(--card-h);
    background: var(--card);
    border-bottom: 6px solid var(--cyan);
    box-shadow: 0 18px 40px rgba(0,0,0,0.18);
  }
  .card--front { top: 120px; }
  .card--back { top: 565px; }

  .brand { display: flex; align-items: center; gap: 18px; }
  .brand__dot {
    flex: none;
    border-radius: 50%;
    background: linear-gradient(135deg, var(--cyan), var(--blue));
  }
  .brand__name {
    font-weight: 500;
    text-transform: uppercase;
    letter-spacing: 0.06em;
    line-height: 1.02;
    color: var(--ink);
  }

  .card--front .brand { position: absolute; left: 130px; top: 44px; }
  .card--front .brand__dot { width: 78px; height: 78px; }
  .card--front .brand__name { font-size: 27px; }

  .contact { position: absolute; left: 52px; top: 172px; right: 52px; }
  .contact__name { color: var(--cyan); font-weight: 700; font-size: 24px; }
  .contact__role { font-size: 14px; margin-top: 2px; }
  .contact__rule { height: 1.5px; background: var(--cyan); margin: 12px 0 14px; }
  .contact__list { list-style: none; font-size: 13.5px; }
  .contact__list li { display: flex; align-items: center; gap: 10px; margin-bottom: 6px; }
  .contact__list svg { width: 13px; height: 13px; flex: none; fill: var(--blue); }

  .card--back .brand { position: absolute; left: 50%; top: 50%; transform: translate(-50%, -50%); gap: 24px; }
  .card--back .brand__dot { width: 120px; height: 120px; }
  .card--back .brand__name { font-size: 38px; }
</style>
</head>
<body>
  <section class="card card--front">
    <div class="brand">
      <span class="brand__dot"></span>
      <span class="brand__name">Kestrel Bridge<br>Consulting</span>
    </div>
    <div class="contact">
      <p class="contact__name">Derek Molvane</p>
      <p class="contact__role">Managing Director</p>
      <div class="contact__rule"></div>
      <ul class="contact__list">
        <li>
          <svg viewBox="0 0 24 24" aria-hidden="true"><path d="M6.6 10.8a15.1 15.1 0 0 0 6.6 6.6l2.2-2.2a1 1 0 0 1 1-.25 11.4 11.4 0 0 0 3.6.57 1 1 0 0 1 1 1V20a1 1 0 0 1-1 1A17 17 0 0 1 3 4a1 1 0 0 1 1-1h3.5a1 1 0 0 1 1 1c0 1.25.2 2.45.57 3.57a1 1 0 0 1-.25 1z"/></svg>
          +1 (555) 218-4907
        </li>
        <li>
          <svg viewBox="0 0 24 24" aria-hidden="true"><path d="M2 5h20v14H2z M2 5l10 8 10-8" /></svg>
          Derek.Molvane@KestrelBridgeConsulting.example
        </li>
        <li>
          <svg viewBox="0 0 24 24" aria-hidden="true"><circle cx="12" cy="12" r="10"/></svg>
          www.KestrelBridgeConsulting.example
        </li>
      </ul>
    </div>
  </section>

  <section class="card card--back">
    <div class="brand">
      <span class="brand__dot"></span>
      <span class="brand__name">Kestrel Bridge<br>Consulting</span>
    </div>
  </section>
</body>
</html>
```